Pet sitting and Dog Walking Postcard distributed to new home owners in our target market

We need a two-sided postcard (or rack card, size can be anything rack card size or smaller) that is going in a folder that will be distributed each month to new homeowners in our target area. I would like the design to be similar to our brochure which will be uploaded here for you to see. It needs much less information than the brochure.
Should include services we offer; and our 4 systems: online registration, complimentary consultation, flexible scheduling, visits with reports and photos. Should also include our contact information (website, email, phone). Photos from the brochure can be used. Tagline from the cover of the brochure can be used. Call to action should be: Register on our website today to receive a free consultation and $20 off your first booking (when requesting a service, mention the promo code: welcome20).

```html
<!DOCTYPE html>
<html lang="en">
<head>
<meta charset="utf-8">
<title>Tailwise Pet Care – Postcard</title>
<link rel="stylesheet" href="https://fonts.googleapis.com/css2?family=Montserrat:wght@300;400;600;700;800&family=Source+Sans+3:ital,wght@0,400;0,600;0,700;1,400&display=swap">
<style>
  :root {
    --plum: #56405f;
    --green: #4f9d3c;
    --green-bright: #5cbf3f;
    --ink: #4c3a55;
    --grey-label: #cfcfcf;
    --page: #ffffff;
  }
  * { box-sizing: border-box; margin: 0; padding: 0; }
  html, body { width: 1200px; height: 1200px; overflow: hidden; background: var(--page); }
  .canvas { position: relative; width: 1200px; height: 1200px; font-family: "Montserrat", sans-serif; }

  .side-label {
    position: absolute; font-family: "Montserrat", sans-serif; font-weight: 400;
    color: var(--grey-label); font-size: 104px; letter-spacing: 4px; line-height: 1;
    transform-origin: left top; transform: rotate(-90deg); white-space: nowrap;
  }
  .side-label--front { left: 56px; top: 598px; }
  .side-label--back { left: 1036px; top: 1180px; }

  /* FRONT */
  .card-front { position: absolute; left: 186px; top: 30px; width: 812px; height: 574px; overflow: hidden;
    background: linear-gradient(90deg, #ffffff 0%, #fbf8f5 45%, #efe6dd 55%, #f7f2ec 62%, #ffffff 80%); }
  .front-backdrop { position: absolute; inset: 0; }
  .tagline { position: absolute; left: -2px; top: 52px; width: 400px; text-align: center;
    font-family: "Source Sans 3", sans-serif; font-weight: 700; font-size: 27px; line-height: 37px; }
  .tagline .line-1 { color: var(--plum); display: block; }
  .tagline .line-2 { color: var(--green); display: block; }
  .brand { position: absolute; display: flex; align-items: center; justify-content: center; gap: 8px; white-space: nowrap; }
  .card-front .brand { left: 552px; top: 130px; width: 200px; }
  .brand-dot { width: 14px; height: 14px; border-radius: 50%; background: var(--plum); flex: none; }
  .brand-name { font-family: "Montserrat", sans-serif; font-weight: 700; font-size: 19px; color: var(--plum); letter-spacing: 0.5px; }
  .photo-ring { position: absolute; left: 0; top: 0; }
  .offer { position: absolute; right: 38px; text-align: right; color: var(--ink); }
  .offer-intro { top: 231px; font-weight: 400; font-size: 17px; letter-spacing: 0.5px; white-space: nowrap; }
  .offer-consult { top: 254px; font-weight: 800; font-size: 29px; letter-spacing: 0.8px; }
  .offer-get { left: 515px; right: auto; top: 316px; font-weight: 300; font-size: 28px; color: #555; }
  .offer-amount { top: 342px; font-weight: 800; font-size: 58px; color: var(--green); letter-spacing: 1px; line-height: 1; }
  .offer-note { top: 405px; font-size: 13.5px; letter-spacing: 0.5px; }
  .promo { position: absolute; right: 38px; top: 448px; border: 1.5px solid var(--green); padding: 2px 4px;
    font-size: 13.5px; letter-spacing: 0.6px; color: var(--ink); }
  .site-url { position: absolute; right: 36px; top: 518px; font-weight: 600; font-size: 19px; letter-spacing: 1.6px; color: var(--plum); }

  /* BACK */
  .card-back { position: absolute; left: 186px; top: 609px; width: 812px; height: 576px; overflow: hidden; }
  .systems-panel { position: absolute; left: 0; top: 0; width: 374px; height: 576px; background: var(--plum); color: #fff; }
  .systems-title { position: absolute; left: 40px; top: 71px; font-family: "Source Sans 3", sans-serif; font-weight: 700; font-size: 22px; white-space: nowrap; }
  .systems-title em { font-style: normal; color: var(--green-bright); }
  .systems-intro { position: absolute; left: 40px; top: 115px; width: 300px; font-family: "Source Sans 3", sans-serif; font-size: 10.6px; line-height: 13px; }
  .system { position: absolute; left: 40px; width: 300px; }
  .system-icon { position: absolute; left: 0; top: 0; width: 42px; height: 42px; border-radius: 50%; background: #fff;
    display: flex; align-items: center; justify-content: center; }
  .system-name { position: absolute; left: 67px; top: -9px; font-family: "Source Sans 3", sans-serif; font-weight: 700; font-size: 12.5px; color: var(--green-bright); white-space: nowrap; }
  .system-text { position: absolute; left: 67px; top: 9px; width: 236px; font-family: "Source Sans 3", sans-serif; font-style: italic; font-size: 10.3px; line-height: 13px; }

  .contact-side { position: absolute; left: 374px; top: 0; width: 438px; height: 576px;
    background: linear-gradient(180deg, #ececed 0%, #f4f4f5 50%, #f8f8f8 100%); }
  .contact-side .brand { left: 123px; top: 242px; width: 200px; }
  .contact-heading { position: absolute; left: 97px; top: 436px; font-weight: 700; font-size: 10.5px; letter-spacing: 0.8px; color: #3f3346; }
  .contact-box { position: absolute; left: 96px; top: 457px; width: 262px; height: 83px; border: 2px solid var(--plum); border-radius: 3px; }
  .contact-row { position: absolute; left: -10px; display: flex; align-items: center; gap: 6px;
    font-family: "Source Sans 3", sans-serif; font-size: 12px; color: #3f3346; }
  .contact-icon { width: 17px; height: 17px; border-radius: 50%; background: var(--plum); display: flex; align-items: center; justify-content: center; }
</style>
</head>
<body>
<div class="canvas">
  <div class="side-label side-label--front">FRONT</div>
  <div class="side-label side-label--back">BACK</div>

  <section class="card-front">
    <div class="front-backdrop" role="img" aria-label="Softly blurred bright living room window in the background"></div>
    <h1 class="tagline"><span class="line-1">Prioritize Yourself.</span><span class="line-2">We'll Focus on Your Pets.</span></h1>
    <div class="brand"><span class="brand-dot"></span><span class="brand-name">Tailwise Pet Care</span></div>

    <svg class="photo-ring" width="812" height="574" viewBox="0 0 812 574">
      <defs>
        <clipPath id="hero-clip"><circle cx="183" cy="406" r="215"/></clipPath>
        <radialGradient id="hero-tone" cx="45%" cy="45%" r="60%">
          <stop offset="0" stop-color="#e9d8c3"/>
          <stop offset="0.6" stop-color="#cdb79f"/>
          <stop offset="1" stop-color="#8e7e78"/>
        </radialGradient>
      </defs>
      <g role="img" aria-label="Photo of a smiling woman on a sofa hugging her brown and white spaniel">
        <rect x="-40" y="180" width="450" height="460" fill="url(#hero-tone)" clip-path="url(#hero-clip)"/>
      </g>
      <circle cx="183" cy="406" r="220" fill="none" stroke="var(--plum)" stroke-width="11"/>
      <path d="M 100 183 A 238 238 0 0 1 352 574" fill="none" stroke="var(--green)" stroke-width="4"/>
    </svg>

    <p class="offer offer-intro">Register on our website today to receive a</p>
    <p class="offer offer-consult">free consultation</p>
    <p class="offer offer-get">Get</p>
    <p class="offer offer-amount">20$ OFF</p>
    <p class="offer offer-note">your first booking</p>
    <p class="promo">PROMO CODE: WELCOME20</p>
    <p class="site-url">www.tailwisepets.com</p>
  </section>

  <section class="card-back">
    <div class="systems-panel">
      <h2 class="systems-title">Ready To Free Up <em>Your Time?</em></h2>
      <p class="systems-intro">We are here to uncomplicate your life! Our systems and processes allow for seamless scheduling, service and billing. Give us a few minutes of your time and we will deliver it back to you tenfold!</p>

      <div class="system" style="top:195px">
        <div class="system-icon"><svg width="22" height="18" viewBox="0 0 22 18"><rect x="1" y="1" width="20" height="13" rx="1" fill="#4a4f6a"/><rect x="3" y="3" width="16" height="9" fill="#dfe6ee"/><rect x="8" y="14" width="6" height="3" fill="#4a4f6a"/></svg></div>
        <h3 class="system-name">Online Registration</h3>
        <p class="system-text">Click on the register link on our homepage to begin online registration or submit a request form if you would like more information first.</p>
      </div>
      <div class="system" style="top:270px">
        <div class="system-icon"><svg width="22" height="20" viewBox="0 0 22 20"><circle cx="14" cy="8" r="7" fill="var(--green)"/><circle cx="9" cy="11" r="8" fill="#3f3346"/><circle cx="6" cy="11" r="1.2" fill="#fff"/><circle cx="9" cy="11" r="1.2" fill="#fff"/><circle cx="12" cy="11" r="1.2" fill="#fff"/></svg></div>
        <h3 class="system-name">Complimentary Consultation</h3>
        <p class="system-text">Request a consultation through our online portal. We'll reach out to you if you get stuck! Then we'll coordinate a meeting at your convenience.</p>
      </div>
      <div class="system" style="top:351px">
        <div class="system-icon"><svg width="22" height="18" viewBox="0 0 22 18"><rect x="1" y="2" width="20" height="15" fill="#eef3ea" stroke="#4a4f6a"/><rect x="1" y="2" width="20" height="3" fill="#4a4f6a"/><g fill="var(--green)"><rect x="4" y="7" width="2" height="2"/><rect x="8" y="7" width="2" height="2"/><rect x="12" y="7" width="2" height="2"/><rect x="4" y="11" width="2" height="2"/><rect x="8" y="11" width="2" height="2"/></g></svg></div>
        <h3 class="system-name">Flexible Scheduling</h3>
        <p class="system-text">Once we've met, we will be able to custom schedule your visits to fit your needs. You can always adjust your schedule through our portal app if your needs change.</p>
      </div>
      <div class="system" style="top:439px">
        <div class="system-icon"><svg width="22" height="18" viewBox="0 0 22 18"><rect x="1" y="4" width="20" height="13" rx="2" fill="#3f4560"/><rect x="7" y="1" width="8" height="4" fill="#3f4560"/><circle cx="11" cy="10.5" r="4.5" fill="#6f8ad0"/><circle cx="11" cy="10.5" r="2" fill="#2a2f45"/></svg></div>
        <h3 class="system-name">Visits with Reports and Photos</h3>
        <p class="system-text">Your pets will be cared for by our elite team of Pet Care Specialists. After each visit, you will receive an emailed report with photo.</p>
      </div>
    </div>

    <div class="contact-side">
      <div class="brand"><span class="brand-dot"></span><span class="brand-name">Tailwise Pet Care</span></div>
      <p class="contact-heading">CONTACT US</p>
      <div class="contact-box">
        <div class="contact-row" style="top:7px"><span class="contact-icon"><svg width="9" height="9" viewBox="0 0 10 10"><path d="M2 1 L4 1 L4.6 3 L3.4 4 Q4.5 6 6 6.6 L7 5.4 L9 6 L9 8 Q5 9 1 4 Q1 2 2 1Z" fill="#fff"/></svg></span>555-010-PAWS</div>
        <div class="contact-row" style="top:31px"><span class="contact-icon"><svg width="10" height="8" viewBox="0 0 10 8"><rect x="0.5" y="0.5" width="9" height="7" fill="none" stroke="#fff"/><path d="M0.5 0.5 L5 4.5 L9.5 0.5" fill="none" stroke="#fff"/></svg></span>hello@tailwisepets.com</div>
        <div class="contact-row" style="top:56px"><span class="contact-icon"><svg width="10" height="10" viewBox="0 0 10 10"><circle cx="5" cy="5" r="4.3" fill="none" stroke="#fff"/><ellipse cx="5" cy="5" rx="2" ry="4.3" fill="none" stroke="#fff"/><path d="M0.7 5 H9.3" stroke="#fff"/></svg></span>www.tailwisepets.com</div>
      </div>
    </div>
  </section>
</div>
</body>
</html>
```